design a construction company business card

Design business card around our logo. Card must have all the typical info: name, title, address, phone, email, business name, etc. Somewhere on the card I would like to see our motto "Built on honesty... Driven by dedication." Consider adding a splash of bright orange to the card to complement the blues and silvers/grays in the logo. We are open to metallic inks, textures, etc. We would like to see options on both light and dark backgrounds. The font in the logo is Euro Technic Extended Regular.

```html
<!DOCTYPE html>
<html lang="en">
<head>
<meta charset="utf-8">
<title>Harlow Contracting, Inc. – Business Card</title>
<link rel="stylesheet" href="https://fonts.googleapis.com/css2?family=Antonio:wght@600&family=Michroma&display=swap">
<style>
  :root {
    --card-bg: #d3d3d1;
    --card-bg-light: #dfdfdd;
    --ink-blue: #1d5291;
    --accent-orange: #e8740f;
    --skyline-blue: #8fa8cc;
    --skyline-grey: #b5b5b5;
  }
  html, body {
    margin: 0;
    padding: 0;
    overflow: hidden;
    background: #ffffff;
  }
  .card {
    position: relative;
    width: 1200px;
    height: 494px;
    overflow: hidden;
    background: radial-gradient(ellipse at 50% 40%, var(--card-bg-light) 0%, var(--card-bg) 75%);
    font-family: "Antonio", "Arial Narrow", sans-serif;
  }
  .skyline {
    position: absolute;
    left: 0;
    top: 0;
  }
  .brand {
    position: absolute;
    top: 30px;
    left: 0;
    width: 100%;
    display: flex;
    justify-content: center;
    align-items: center;
    gap: 12px;
  }
  .brand-mark {
    width: 22px;
    height: 22px;
    background: var(--ink-blue);
  }
  .brand-name {
    font-weight: 600;
    font-size: 46px;
    line-height: 1;
    color: var(--ink-blue);
    letter-spacing: 1px;
  }
  .contact {
    position: absolute;
    top: 112px;
    margin: 0;
    padding: 0;
    list-style: none;
    font-weight: 600;
    font-size: 48px;
    line-height: 70px;
    white-space: nowrap;
    color: var(--ink-blue);
    text-shadow: 1px 2px 3px rgba(18, 58, 106, 0.45);
  }
  .contact-person { left: 80px; text-align: left; }
  .contact-lines { right: 78px; text-align: right; }
  .motto {
    position: absolute;
    top: 434px;
    margin: 0;
    font-family: "Michroma", "Arial", sans-serif;
    font-size: 27px;
    font-weight: 400;
    letter-spacing: 1px;
    white-space: nowrap;
    color: var(--accent-orange);
    text-shadow: 1px 1px 2px rgba(120, 50, 0, 0.35);
  }
  .motto-left { left: 80px; }
  .motto-right { right: 78px; }
</style>
</head>
<body>
  <div class="card">
    <svg class="skyline" width="1200" height="494" viewBox="0 0 1200 494">
      <defs>
        <linearGradient id="skylineFill" x1="0" y1="0" x2="0" y2="1">
          <stop offset="0" stop-color="#8fa8cc" stop-opacity="0.55"/>
          <stop offset="1" stop-color="#b5b5b5" stop-opacity="0.75"/>
        </linearGradient>
      </defs>
      <line x1="216" y1="401" x2="502" y2="401" stroke="#8fa8cc" stroke-width="4"/>
      <line x1="729" y1="401" x2="986" y2="401" stroke="#8fa8cc" stroke-width="4"/>
      <rect x="502" y="161" width="227" height="242" fill="url(#skylineFill)" role="img" aria-label="Faint skyline of construction towers"/>
    </svg>

    <header class="brand">
      <span class="brand-mark"></span>
      <span class="brand-name">Harlow Contracting, Inc.</span>
    </header>

    <ul class="contact contact-person">
      <li class="contact-name">Sam Keller</li>
      <li class="contact-title">Estimator</li>
      <li class="contact-address">12 Quarry Lane, Ashford VIC</li>
    </ul>

    <ul class="contact contact-lines">
      <li class="contact-mobile">0412555018</li>
      <li class="contact-phone">0255501234</li>
      <li class="contact-email">sam@harlowbuild.com</li>
    </ul>

    <p class="motto motto-left">Built on honesty</p>
    <p class="motto motto-right">Driven by dedication</p>
  </div>
</body>
</html>
```